Clean, Fresh Business Card Design Needed

We need a business card design for a new business we have taken over called "Bonders and Fixers". We got a logo through this website which i have attached. We are wanting something that is vibrant but clean and fresh. Our business mainly sells glue. Maybe a cool design/slogan on the back? Modern, sleek.

Industry/Entity Type

Business

Contact Information for Business Card

Name: Derek Tamsin, Managing Director. Address: 164 Kowhai Lane, Tauranga 3112, Phone: 07 549 2361 Mobile: 021 634 915 Fax: 07 549 2874 Email: bond.fix@mailvo.co.nz, Web: www.tackbondpro.co.nz

Font styles to use
Serif

Requirements
Must have
• All business card details, logo.
Nice to have
• Design, slogan on back of card

```html
<!DOCTYPE html>
<html lang="en">
<head>
<meta charset="utf-8">
<title>Bonders and Fixers – Business Card</title>
<link href="https://fonts.googleapis.com/css2?family=Exo+2:wght@400;500&display=swap" rel="stylesheet">
<style>
  :root {
    --stage: #e4e6ee;
    --card: #ffffff;
    --card-shade: #eeeeef;
    --ink-dark: #262626;
    --accent-blue: #3d4a8e;
    --text-light: #ffffff;
    --text-dark: #2a2a2a;
  }
  html, body {
    margin: 0;
    width: 1200px;
    height: 840px;
    overflow: hidden;
    background: var(--stage);
    font-family: "Exo 2", sans-serif;
  }
  .stage {
    width: 1200px;
    height: 840px;
    display: flex;
    align-items: center;
    justify-content: center;
  }
  .business-card {
    position: relative;
    width: 1000px;
    height: 571px;
    background: linear-gradient(160deg, var(--card) 40%, var(--card-shade) 100%);
    box-shadow: 0 10px 30px rgba(40, 45, 70, 0.18);
    overflow: hidden;
  }
  .card-art {
    position: absolute;
    inset: 0;
    width: 100%;
    height: 100%;
  }
  .card-art .top-band { fill: var(--ink-dark); }
  .card-art .accent-line {
    fill: none;
    stroke: var(--accent-blue);
    stroke-width: 6;
  }

  .holder {
    position: absolute;
    top: 40px;
    right: 40px;
    text-align: right;
    color: var(--text-light);
  }
  .holder-name {
    margin: 0;
    font-size: 36px;
    font-weight: 500;
    letter-spacing: 1.5px;
    text-transform: uppercase;
  }
  .holder-title {
    margin: 4px 0 0;
    font-size: 24px;
    font-weight: 400;
    letter-spacing: 0.5px;
  }

  .brand {
    position: absolute;
    left: 46px;
    top: 292px;
    display: flex;
    align-items: center;
    gap: 14px;
  }
  .brand-mark {
    width: 56px;
    height: 56px;
    background: var(--accent-blue);
  }
  .brand-name {
    font-size: 34px;
    font-weight: 400;
    color: var(--accent-blue);
    letter-spacing: 1px;
  }

  .address {
    position: absolute;
    right: 40px;
    top: 298px;
    margin: 0;
    text-align: right;
    font-style: normal;
    font-size: 24px;
    line-height: 1.3;
    letter-spacing: 1px;
    color: var(--text-dark);
  }

  .contact-list {
    position: absolute;
    left: 46px;
    bottom: 30px;
    margin: 0;
    padding: 0;
    list-style: none;
    font-size: 19px;
    letter-spacing: 0.8px;
    color: var(--text-dark);
  }
  .contact-list li {
    display: flex;
    align-items: center;
    gap: 12px;
    height: 33px;
  }
  .contact-icon {
    width: 20px;
    height: 20px;
    fill: var(--text-dark);
    flex: none;
  }
</style>
</head>
<body>
<main class="stage">
  <article class="business-card">
    <svg class="card-art" viewBox="0 0 1000 571" preserveAspectRatio="none" aria-hidden="true">
      <path class="top-band" d="M0 0 H1000 V150 Q500 230 0 170 Z"/>
      <path class="accent-line" d="M0 192 Q500 252 1000 172"/>
    </svg>

    <header class="holder">
      <h1 class="holder-name">Derek Tamsin</h1>
      <p class="holder-title">Managing Director</p>
    </header>

    <div class="brand">
      <span class="brand-mark"></span>
      <span class="brand-name">Bonders and Fixers</span>
    </div>

    <address class="address">164 Kowhai Lane<br>Tauranga 3112</address>

    <ul class="contact-list">
      <li>
        <svg class="contact-icon" viewBox="0 0 24 24" aria-label="Phone"><path d="M6.6 10.8a15.1 15.1 0 0 0 6.6 6.6l2.2-2.2a1 1 0 0 1 1-.25 11.4 11.4 0 0 0 3.6.57 1 1 0 0 1 1 1V20a1 1 0 0 1-1 1A17 17 0 0 1 3 4a1 1 0 0 1 1-1h3.5a1 1 0 0 1 1 1c0 1.25.2 2.45.57 3.57a1 1 0 0 1-.25 1z"/></svg>
        07 549 2361
      </li>
      <li>
        <svg class="contact-icon" viewBox="0 0 24 24" aria-label="Mobile"><path d="M7 1h10a2 2 0 0 1 2 2v18a2 2 0 0 1-2 2H7a2 2 0 0 1-2-2V3a2 2 0 0 1 2-2zm0 3v14h10V4zm5 15.5a1 1 0 1 0 0 2 1 1 0 0 0 0-2z"/></svg>
        021 634 915
      </li>
      <li>
        <svg class="contact-icon" viewBox="0 0 24 24" aria-label="Fax"><path d="M7 2h8l3 3v5h2a2 2 0 0 1 2 2v8a2 2 0 0 1-2 2H4a2 2 0 0 1-2-2v-8a2 2 0 0 1 2-2h3zm2 2v6h7V6h-2V4zM5 14v2h3v-2zm5 0v2h3v-2zm5 0v2h3v-2zM5 18v2h3v-2zm5 0v2h3v-2zm5 0v2h3v-2z"/></svg>
        07 549 2874
      </li>
      <li>
        <svg class="contact-icon" viewBox="0 0 24 24" aria-label="Email"><path d="M2 5h20v14H2zm2 2v.5l8 5 8-5V7zm0 2.9V17h16V9.9l-8 5z"/></svg>
        bond.fix@mailvo.co.nz
      </li>
      <li>
        <svg class="contact-icon" viewBox="0 0 24 24" aria-label="Website"><path d="M12 2a10 10 0 1 0 0 20 10 10 0 0 0 0-20zm6.9 6h-3a15 15 0 0 0-1.3-3.9A8 8 0 0 1 18.9 8zM12 4c.9 1.2 1.600 2.6 2 4h-4c.4-1.4 1.1-2.8 2-4zM4.3 14a8 8 0 0 1 0-4h3.4a16 16 0 0 0 0 4zm.8 2h3a15 15 0 0 0 1.3 3.9A8 8 0 0 1 5.1 16zm3-8h-3a8 8 0 0 1 4.3-3.9A15 15 0 0 0 8.1 8zM12 20c-.9-1.2-1.6-2.6-2-4h4c-.4 1.4-1.1 2.8-2 4zm2.3-6H9.7a14 14 0 0 1 0-4h4.6a14 14 0 0 1 0 4zm.3 5.9A15 15 0 0 0 15.9 16h3a8 8 0 0 1-4.3 3.9zm1.7-5.9a16 16 0 0 0 0-4h3.4a8 8 0 0 1 0 4z"/></svg>
        www.tackbondpro.co.nz
      </li>
    </ul>
  </article>
</main>
</body>
</html>
```